Style Template created - Report Accounting and Advisory industry

We need a style template created to set out a report for advice. The report follows <br/><br/>- Cover Page - ( we would need to print to a letter head )<br/>- General Disclaimer<br/>- Space to add Excel Reports in to the document- Maybe inserted Pdf's later<br/>- Action Plan dot points under headings<br/>- List of Strategies to be adopted<br/><br/>Attached is a quick example word doc that needs Custom Style Templates made so that we can quickly format items added. Also the ugly PDF that we currently produce for clients <br/><br/>Red - is our preferred Colour<br/><br/>

Target Market(s)

Accounting / Business / Professionals

Industry/Entity Type

Accounting

Colors
ec1f27

Requirements
Nice to have
• Simple Clean design. Not to busy. Easy to modify the "wording text" in design
Should not have
• Too busy or too much color

```html
<!DOCTYPE html>
<html lang="en">
<head>
<meta charset="utf-8">
<title>Halden Reeve – Report Style Template</title>
<link href="https://fonts.googleapis.com/css2?family=Open+Sans:ital,wght@0,400;0,600;0,700;1,400&family=Cormorant+SC:wght@500;600&display=swap" rel="stylesheet">
<style>
:root{
  --red:#ec1f27;
  --deep-red:#c4141b;
  --ink:#3a3a3a;
  --muted:#6b6b6b;
  --rule:#cfcfcf;
  --board:#4a4a4a;
  --paper:#ffffff;
  --black:#161616;
  --grey-box:#d3d3d3;
}
*{margin:0;padding:0;box-sizing:border-box}
html,body{width:858px;height:1200px;overflow:hidden;background:var(--board)}
body{position:relative;font-family:"Open Sans",Arial,sans-serif;color:var(--ink)}
.page{position:absolute;width:270px;height:382px;background:var(--paper);overflow:hidden}
.c1{left:14px}.c2{left:293px}.c3{left:572px}
.r1{top:10px}.r2{top:405px}.r3{top:799px}

/* red pages */
.red-page{background:radial-gradient(circle at 55% 30%,#d8262c 0%,#c3161c 45%,#a90e13 100%);color:#fff}

/* wordmark: plain sans text with one small square */
.brand{display:flex;align-items:center;gap:4px;font-family:"Open Sans",Arial,sans-serif;font-weight:600;line-height:1;white-space:nowrap}
.brand::before{content:"";display:block;width:.55em;height:.55em;background:currentColor}
.cover-brand{position:absolute;right:16px;top:48px;font-size:18px}
.divider-brand,.band-brand{position:absolute;right:12px;top:18px;font-size:12px;color:#fff}
.head-brand{font-size:9px;color:var(--ink);margin-top:4px}

.cover-title{position:absolute;right:16px;top:251px;text-align:right;font-weight:700;font-size:17px;line-height:23px}
.cover-client{position:absolute;right:24px;top:323px;font-size:12px;letter-spacing:.4px}
.divider-title{position:absolute;left:24px;top:182px;font-weight:700;font-size:12.5px;line-height:16px;letter-spacing:.2px;color:#fff}

/* inner pages */
.stripe{position:absolute;left:0;top:0;width:13px;height:100%;background:var(--red)}
.stripe::before{content:"";position:absolute;left:0;top:0;width:13px;height:25px;background:var(--black)}
.head{position:absolute;left:23px;right:8px;top:8px;display:flex;justify-content:space-between;align-items:flex-start}
.project{font-family:"Cormorant SC",Georgia,serif;font-weight:600;color:var(--red);font-size:13px;letter-spacing:.5px}
.foot{position:absolute;left:23px;right:10px;bottom:18px;border-top:.6px solid var(--rule);padding-top:4px;text-align:center;font-size:5px;color:var(--ink)}
.body{position:absolute;left:23px;right:10px;top:34px}
h2{color:var(--red);font-size:6.4px;font-weight:700;margin:0 0 3px}
h3{color:var(--red);font-size:4.6px;font-weight:700;margin:5px 0 2px}
p{font-size:4.4px;line-height:6.6px;margin-bottom:3px}
.tiny p,.tiny li{font-size:3.1px;line-height:4.6px}
.tiny ul{margin:1px 0 3px 6px}
.tiny li{list-style:disc}
.quote-band{background:var(--deep-red);color:#fff;font-style:italic;font-size:8px;padding:4px 9px;margin:7px 0 7px;width:220px}
.red-text{color:var(--red)}
.italic-red{color:var(--red);font-style:italic}
.cols{display:flex;gap:8px}
.cols>div{flex:1}

/* tables */
.tbl{width:100%;border-collapse:collapse;font-size:4.2px;margin:3px 0 10px}
.tbl th{font-weight:600;text-align:left;padding:3px 3px}
.tbl td{padding:2.3px 3px}
.tbl td:first-child,.tbl th:first-child{width:64px}
.t1 thead tr{border-top:.8px solid var(--red);border-bottom:.6px solid var(--red)}
.t1 tbody tr:last-child{border-bottom:.6px solid #f2a3a6}
.t2 thead tr{background:#e4e4e4}
.t3{border:.8px solid var(--red)}
.t3 thead tr{background:var(--deep-red);color:#fff}
.h-plain{color:var(--ink);font-weight:600}

/* toc */
.toc{position:absolute;left:28px;right:10px;top:42px;list-style:none}
.toc li{display:flex;align-items:baseline;font-size:7px;height:20.4px}
.toc .dots{flex:1;border-bottom:.8px dotted #777;margin:0 4px 0 3px}
.toc .num{width:16px;text-align:right}

/* page 7 */
.photo-band{position:absolute;left:0;top:0;width:100%;height:139px;background:linear-gradient(180deg,#c81a20 0%,#b0141a 55%,#9a1015 100%)}
.band-text{position:absolute;left:17px;right:14px;top:63px;color:#fff;font-style:italic;font-size:6.4px;line-height:11px}
.lower{position:absolute;left:17px;right:14px;top:156px}
.lower h2{margin-top:14px}
.lower h2:first-child{margin-top:0}
.plain-foot{position:absolute;left:17px;right:14px;bottom:8px;border-top:.6px solid var(--rule);padding-top:4px;text-align:center;font-size:5px}

/* page 9 */
.split{display:flex;gap:8px;margin-bottom:26px}
.split .txt{width:120px}
.img-box{width:116px;height:108px;background:var(--grey-box);margin-top:3px}
</style>
</head>
<body>

<section class="page c1 r1 red-page" aria-label="Cover page">
  <div class="brand cover-brand">Halden Reeve</div>
  <h1 class="cover-title">Taxation Projection<br>&amp; Planning - 2020</h1>
  <div class="cover-client">Client Name</div>
</section>

<section class="page c2 r1">
  <div class="stripe"></div>
  <header class="head"><div class="project">Project Title Here</div><div class="brand head-brand">Halden Reeve</div></header>
  <div class="body tiny">
    <h2>Purpose of Tax Planning</h2>
    <h3>Why bother.....???</h3>
    <p>Tax planning is the activities taken to minimise tax liabilities to ensure all available allowances, deductions, exclusions and exemptions are working together in the most tax effective manner to reduce the total tax bill.</p>
    <p>The purpose of this report is to provide a recommendation of strategies for you to consider for the year to come. This report is not intended to be our final advice to you, but instead a starting point in educating you on potential opportunities.</p>
    <div class="quote-band">“If you fail to plan, you are planning to fail”</div>
    <p class="red-text">Tax planning strategies are typically employed to help a business achieve their financial and business goals. The benefits of tax planning are:</p>
    <ul><li>Lowering the Amount of taxable income</li><li>Reducing the tax rate</li><li>Allowing greater Control of when taxes get paid</li><li>Better Management of your cashflow</li><li>Eliminating nasty tax surprises</li></ul>
    <h3>Recommendations</h3>
    <p>We will provide you with a list of Action plans and a further list of ........ The list will be broken down in Short term and Longer Term action. Also list of actions to follow up on ......work on this list .....sp.</p>
    <h3>Basis of Preparation</h3>
    <p>The taxation estimate has been prepared on the basis of information provided by the client. The report is intended for internal tax planning purposes and represents a “What if scenario”. It does not necessarily represent real or intended transactions. HaldenReeve have not performed any tests to verify or validate any of the information provided by the client and accordingly express no assurance as to the outcome indicated.</p>
    <p>To the extent permitted by law we do not accept liability for any loss or damage which any person, other than the client may suffer arising from any negligence on our part. No person should rely on the Taxation estimate without having a full review or audit conducted on the data.</p>
    <h3>Superannuation</h3>
    <p>Provision of Advice is guided by legislative requirements to be provided in a Statement of Advice. Any and all comments regarding Superannuation are not to be taken as advice rather than statement of factual information about the situation. The statement is not a recommendation to take any action unless that action is required by law. The clients personal situation has not been considered in providing the information. Any action to be taken in relation to the information provided, should take into account the clients personal situation and consideration must be given as to whether action will be appropriate for the clients' objectives and needs. Specific Contribution amounts and SMSF product advice can only be provided under a Statement of Advice by a AFSL Holder.</p>
    <p style="margin-top:10px">HaldenReeve<br><span class="red-text">Chartered Accountants</span></p>
  </div>
  <footer class="foot">Copyright text here</footer>
</section>

<section class="page c3 r1">
  <div class="stripe"></div>
  <header class="head"><div class="project">Project Title Here</div><div class="brand head-brand">Halden Reeve</div></header>
  <div class="body" style="top:42px">
    <h2>Lorem ipsum dolor sit amet</h2>
    <p>Lorem ipsum dolor sit amet, consectetur adipiscing elit, sed do eiusmod tempor incididunt ut labore et dolore magna aliqua. Ut enim ad minim veniam, quis nostrud exercitation ullamco laboris nisi ut aliquip ex ea commodo consequat. Duis aute irure dolor in reprehenderit in voluptate velit esse cillum dolore eu fugiat nulla pariatur. Excepteur sint occaecat cupidatat non proident, sunt in culpa qui officia deserunt mollit anim id est laborum." Sed ut perspiciatis unde omnis iste natus error sit voluptatem accusantium doloremque laudantium, totam rem aperiam, eaque ipsa quae ab illo inventore veritatis et quasi architecto beatae vitae dicta sunt explicabo.</p>
    <p class="italic-red" style="margin-top:7px">Ut enim ad minima veniam, quis nostrum exercitationem ullam corporis suscipit laboriosam, nisi ut aliquid ex ea commodi consequatur? Quis autem vel eum iure reprehenderit qui in ea voluptate velit esse quam nihil molestiae consequatur, vel illum qui dolorem eum fugiat quo voluptas nulla pariatur?"</p>
    <h2 style="margin-top:12px">Lorem ipsum dolor sit amet</h2>
    <div class="cols">
      <div><p>Lorem ipsum dolor sit amet, consectetur adipiscing elit, sed do eiusmod tempor incididunt ut labore et dolore magna aliqua. Ut enim ad minim veniam, quis nostrud exercitation ullamco laboris nisi ut aliquip ex ea commodo consequat. Duis aute irure dolor in reprehenderit in voluptate velit esse cillum dolore eu fugiat nulla pariatur. Excepteur sint occaecat cupidatat non proident, sunt in culpa qui officia deserunt mollit anim id est laborum."</p>
      <p>"Sed ut perspiciatis unde omnis iste natus error sit voluptatem accusantium doloremque laudantium, totam rem aperiam, eaque ipsa quae ab illo inventore veritatis et quasi architecto beatae vitae dicta sunt explicabo. Nemo enim ipsam voluptatem quia voluptas sit aspernatur aut odit aut fugit, sed quia consequuntur magni dolores eos qui ratione voluptatem sequi nesciunt.</p></div>
      <div><p>"Lorem ipsum dolor sit amet, consectetur adipiscing elit, sed do eiusmod tempor incididunt ut labore et dolore magna aliqua. Ut enim ad minim veniam, quis nostrud exercitation ullamco laboris nisi ut aliquip ex ea commodo consequat. Duis aute irure dolor in reprehenderit in voluptate velit esse cillum dolore eu fugiat nulla pariatur. Excepteur sint occaecat cupidatat non proident, sunt in culpa qui officia deserunt mollit anim id est laborum."</p>
      <p>"Sed ut perspiciatis unde omnis iste natus error sit voluptatem accusantium doloremque laudantium, totam rem aperiam, eaque ipsa quae ab illo inventore veritatis et quasi architecto beatae vitae dicta sunt explicabo. Nemo enim ipsam voluptatem quia voluptas sit aspernatur aut odit aut fugit.</p></div>
    </div>
  </div>
  <footer class="foot">Copyright text here</footer>
</section>

<section class="page c1 r2 red-page" aria-label="Section divider">
  <div class="brand divider-brand">Halden Reeve</div>
  <h2 class="divider-title">SECTION DIVIDER<br>TITE HERE</h2>
</section>

<section class="page c2 r2">
  <div class="stripe"></div>
  <header class="head"><div class="project">Project Title Here</div><div class="brand head-brand">Halden Reeve</div></header>
  <div class="body" style="top:42px">
    <h2>Lorem ipsum dolor sit amet</h2>
    <p>Lorem ipsum dolor sit amet, consectetur adipiscing elit, sed do eiusmod tempor incididunt ut labore et dolore magna aliqua. Ut enim ad minim veniam, quis nostrud exercitation ullamco laboris nisi ut aliquip ex ea commodo consequat. Duis aute irure dolor in reprehenderit in voluptate velit esse cillum dolore eu fugiat nulla pariatur. Excepteur sint occaecat cupidatat non proident, sunt in culpa qui officia deserunt mollit anim id est laborum.</p>
    <h2 style="margin-top:9px">Table Style 1</h2>
    <table class="tbl t1"><thead><tr><th>Title 1</th><th>Title 2</th><th>Title 3</th><th>Title 4</th><th>Title 5</th><th>Title 6</th></tr></thead>
      <tbody><tr><td>Lorem ipsum dolor</td><td>xxx</td><td>xxx</td><td>xxx</td><td>xxx</td><td>xxx</td></tr><tr><td>Lorem ipsum dolor</td><td>xxx</td><td>xxx</td><td>xxx</td><td>xxx</td><td>xxx</td></tr><tr><td>Lorem ipsum dolor</td><td>xxx</td><td>xxx</td><td>xxx</td><td>xxx</td><td>xxx</td></tr><tr><td>Lorem ipsum dolor</td><td>xxx</td><td>xxx</td><td>xxx</td><td>xxx</td><td>xxx</td></tr></tbody></table>
    <h2 class="h-plain">Table Style 2</h2>
    <table class="tbl t2"><thead><tr><th>Title 1</th><th>Title 2</th><th>Title 3</th><th>Title 4</th><th>Title 5</th><th>Title 6</th></tr></thead>
      <tbody><tr><td>Lorem ipsum dolor</td><td>xxx</td><td>xxx</td><td>xxx</td><td>xxx</td><td>xxx</td></tr><tr><td>Lorem ipsum dolor</td><td>xxx</td><td>xxx</td><td>xxx</td><td>xxx</td><td>xxx</td></tr><tr><td>Lorem ipsum dolor</td><td>xxx</td><td>xxx</td><td>xxx</td><td>xxx</td><td>xxx</td></tr><tr><td>Lorem ipsum dolor</td><td>xxx</td><td>xxx</td><td>xxx</td><td>xxx</td><td>xxx</td></tr></tbody></table>
    <h2>Table Style 3</h2>
    <table class="tbl t3"><thead><tr><th>Title 1</th><th>Title 2</th><th>Title 3</th><th>Title 4</th><th>Title 5</th><th>Title 6</th></tr></thead>
      <tbody><tr><td>Lorem ipsum dolor</td><td>xxx</td><td>xxx</td><td>xxx</td><td>xxx</td><td>xxx</td></tr><tr><td>Lorem ipsum dolor</td><td>xxx</td><td>xxx</td><td>xxx</td><td>xxx</td><td>xxx</td></tr><tr><td>Lorem ipsum dolor</td><td>xxx</td><td>xxx</td><td>xxx</td><td>xxx</td><td>xxx</td></tr><tr><td>Lorem ipsum dolor</td><td>xxx</td><td>xxx</td><td>xxx</td><td>xxx</td><td>xxx</td></tr></tbody></table>
  </div>
  <footer class="foot">Copyright text here</footer>
</section>

<section class="page c3 r2">
  <div class="stripe"></div>
  <header class="head"><div class="project">Project Title Here</div><div class="brand head-brand">Halden Reeve</div></header>
  <ol class="toc">
    <li>Table of Content<span class="dots"></span><span class="num">01</span></li>
    <li>About US<span class="dots"></span><span class="num">01</span></li>
    <li>Out Graphs<span class="dots"></span><span class="num">01</span></li>
    <li>Table of Content<span class="dots"></span><span class="num">01</span></li>
    <li>Table of Content<span class="dots"></span><span class="num">01</span></li>
    <li>Table of Content<span class="dots"></span><span class="num">01</span></li>
    <li>Table of Content<span class="dots"></span><span class="num">01</span></li>
    <li>Table of Content<span class="dots"></span><span class="num">01</span></li>
    <li>Table of Content<span class="dots"></span><span class="num">01</span></li>
    <li>Table of Content<span class="dots"></span><span class="num">01</span></li>
    <li>Table of Content<span class="dots"></span><span class="num">01</span></li>
    <li>Table of Content<span class="dots"></span><span class="num">01</span></li>
    <li>Table of Content<span class="dots"></span><span class="num">01</span></li>
  </ol>
  <footer class="foot">Copyright text here</footer>
</section>

<section class="page c1 r3">
  <div class="photo-band" role="img" aria-label="Red-toned landscape photograph of a lake and hills"></div>
  <div class="brand band-brand">Halden Reeve</div>
  <p class="band-text">Lorem ipsum dolor sit amet, consectetur adipiscing elit, sed do eiusmod tempor incididunt ut labore et dolore magna aliqua. Ut enim ad minim veniam, quis nostrud exercitation ullamco laboris nisi ut aliquip ex ea commodo consequat. Duis aute irure dolor in reprehenderit in voluptate velit esse cillum dolore eu fugiat nulla pariatur. Excepteur</p>
  <div class="lower">
    <h2>Lorem ipsum dolor sit amet</h2>
    <p>Lorem ipsum dolor sit amet, consectetur adipiscing elit, sed do eiusmod tempor incididunt ut labore et dolore magna aliqua. Ut enim ad minim veniam, quis nostrud exercitation ullamco laboris nisi ut aliquip ex ea commodo consequat. Duis aute irure dolor in reprehenderit in voluptate velit esse cillum dolore eu fugiat nulla pariatur. Excepteur sint occaecat cupidatat non proident, sunt in culpa qui officia deserunt mollit anim id est laborum.</p>
    <h2>Lorem ipsum dolor sit amet</h2>
    <p>Lorem ipsum dolor sit amet, consectetur adipiscing elit, sed do eiusmod tempor incididunt ut labore et dolore magna aliqua. Ut enim ad minim veniam, quis nostrud exercitation ullamco laboris nisi ut aliquip ex ea commodo consequat. Duis aute irure dolor in reprehenderit in voluptate velit esse cillum dolore eu fugiat nulla pariatur. Excepteur sint occaecat cupidatat non proident, sunt in culpa qui officia deserunt mollit anim id est laborum.</p>
    <h2>Lorem ipsum dolor sit amet</h2>
    <p>Lorem ipsum dolor sit amet, consectetur adipiscing elit, sed do eiusmod tempor incididunt ut labore et dolore magna aliqua. Ut enim ad minim veniam, quis nostrud exercitation ullamco laboris nisi ut aliquip ex ea commodo consequat. Duis aute irure dolor in reprehenderit in voluptate velit esse cillum dolore eu fugiat nulla pariatur. Excepteur sint occaecat cupidatat non proident, sunt in culpa qui officia deserunt mollit anim id est laborum.</p>
  </div>
  <footer class="plain-foot">Copyright text here</footer>
</section>

<section class="page c2 r3">
  <div class="stripe"></div>
  <header class="head"><div class="project">Project Title Here</div><div class="brand head-brand">Halden Reeve</div></header>
  <div class="body" style="top:42px">
    <h2>Lorem ipsum dolor sit amet</h2>
    <p>Lorem ipsum dolor sit amet, consectetur adipiscing elit, sed do eiusmod tempor incididunt ut labore et dolore magna aliqua. Ut enim ad minim veniam, quis nostrud exercitation ullamco laboris nisi ut aliquip ex ea commodo consequat. Duis aute irure dolor in reprehenderit in voluptate velit esse cillum dolore eu fugiat nulla pariatur. Excepteur sint occaecat cupidatat non proident, sunt in culpa qui officia deserunt mollit anim id est laborum.</p>
  </div>
  <svg style="position:absolute;left:23px;top:110px" width="240" height="55" viewBox="0 0 240 55" aria-label="Bar chart">
    <rect x="0" y="20" width="19" height="35" fill="#ec1f27"/>
    <rect x="27" y="6" width="19" height="49" fill="#ec1f27"/>
    <rect x="54" y="25" width="19" height="30" fill="#ec1f27"/>
    <rect x="98" y="28" width="17" height="27" fill="#e26a6e"/>
    <rect x="120" y="8" width="17" height="47" fill="#e26a6e"/>
    <rect x="142" y="42" width="17" height="13" fill="#e26a6e"/>
    <rect x="181" y="19" width="17" height="36" fill="#5a5a5a"/>
    <rect x="203" y="0" width="17" height="55" fill="#5a5a5a"/>
    <rect x="225" y="47" width="15" height="8" fill="#5a5a5a"/>
  </svg>
  <div class="body" style="top:197px">
    <h2>PIE chart Title here</h2>
    <p>Lorem ipsum dolor sit amet, consectetur adipiscing elit, sed do eiusmod tempor incididunt ut labore et dolore magna aliqua. Ut enim ad minim veniam sed do eiusmod tempor</p>
  </div>
  <svg style="position:absolute;left:33px;top:238px" width="180" height="112" viewBox="0 0 180 112" aria-label="Line chart">
    <g stroke="#dedede" stroke-width=".5">
      <line x1="10" y1="8" x2="170" y2="8"/><line x1="10" y1="23" x2="170" y2="23"/><line x1="10" y1="38" x2="170" y2="38"/><line x1="10" y1="53" x2="170" y2="53"/><line x1="10" y1="68" x2="170" y2="68"/><line x1="10" y1="83" x2="170" y2="83"/><line x1="10" y1="98" x2="170" y2="98"/>
      <line x1="26" y1="0" x2="26" y2="106"/><line x1="42" y1="0" x2="42" y2="106"/><line x1="58" y1="0" x2="58" y2="106"/><line x1="74" y1="0" x2="74" y2="106"/><line x1="90" y1="0" x2="90" y2="106"/><line x1="106" y1="0" x2="106" y2="106"/><line x1="122" y1="0" x2="122" y2="106"/><line x1="138" y1="0" x2="138" y2="106"/><line x1="154" y1="0" x2="154" y2="106"/><line x1="170" y1="0" x2="170" y2="106"/>
    </g>
    <line x1="10" y1="0" x2="10" y2="106" stroke="#999" stroke-width=".6"/>
    <line x1="10" y1="106" x2="170" y2="106" stroke="#999" stroke-width=".6"/>
    <g font-size="3.5" fill="#999" font-family="Open Sans, sans-serif">
      <text x="3" y="24">5</text><text x="3" y="39">4</text><text x="3" y="54">3</text><text x="3" y="69">2</text><text x="3" y="84">1</text>
    </g>
    <g fill="none" stroke-width="1">
      <path d="M10 105 C25 60 35 40 52 38 S100 20 108 26 S140 60 160 50" stroke="#9e0b12"/>
      <path d="M10 105 C25 80 40 58 52 48 S95 28 108 36 S145 38 160 16" stroke="#ec1f27"/>
      <path d="M10 105 C25 80 40 62 52 58 S95 40 108 46 S145 30 160 28" stroke="#f0767b"/>
      <path d="M10 105 C25 90 40 72 52 68 S95 62 108 60 S130 90 160 72" stroke="#b3b3b3"/>
      <path d="M10 105 C25 92 40 82 52 78 S95 70 108 78 S130 110 160 62" stroke="#e3262e"/>
    </g>
    <g>
      <circle cx="52" cy="38" r="1.6" fill="#9e0b12"/><circle cx="108" cy="26" r="1.6" fill="#9e0b12"/><circle cx="160" cy="50" r="1.6" fill="#9e0b12"/>
      <circle cx="52" cy="48" r="1.6" fill="#ec1f27"/><circle cx="108" cy="36" r="1.6" fill="#ec1f27"/><circle cx="160" cy="16" r="1.6" fill="#ec1f27"/>
      <circle cx="52" cy="58" r="1.6" fill="#f0767b"/><circle cx="108" cy="46" r="1.6" fill="#f0767b"/><circle cx="160" cy="28" r="1.6" fill="#f0767b"/>
      <circle cx="52" cy="68" r="1.6" fill="#b3b3b3"/><circle cx="108" cy="60" r="1.6" fill="#b3b3b3"/><circle cx="160" cy="72" r="1.6" fill="#b3b3b3"/>
      <circle cx="52" cy="78" r="1.6" fill="#e3262e"/><circle cx="10" cy="105" r="1.6" fill="#ec1f27"/>
    </g>
  </svg>
  <footer class="foot">Copyright text here</footer>
</section>

<section class="page c3 r3">
  <div class="stripe"></div>
  <header class="head"><div class="project">Project Title Here</div><div class="brand head-brand">Halden Reeve</div></header>
  <div class="body" style="top:39px">
    <div class="split">
      <div class="txt"><h2>Lorem ipsum dolor sit amet</h2><p>Lorem ipsum dolor sit amet, consectetur adipiscing elit, sed do eiusmod tempor incididunt ut labore et dolore magna aliqua. Ut enim ad minim veniam, quis nostrud exercitation ullamco laboris nisi ut aliquip ex ea commodo consequat. Duis aute irure dolor in reprehenderit in voluptate velit esse cillum dolore eu fugiat nulla pariatur. Excepteur sint occaecat cupidatat non proident, sunt in culpa qui officia deserunt mollit anim id est laborum. updatat non proident, sunt in culpa qui officia deserunt mollit anim id est laborum.</p></div>
      <div class="img-box" role="img" aria-label="Image placeholder"></div>
    </div>
    <div class="split">
      <div class="txt"><h2>Lorem ipsum dolor sit amet</h2><p>Lorem ipsum dolor sit amet, consectetur adipiscing elit, sed do eiusmod tempor incididunt ut labore et dolore magna aliqua. Ut enim ad minim veniam, quis nostrud exercitation ullamco laboris nisi ut aliquip ex ea commodo consequat. Duis aute irure dolor in reprehenderit in voluptate velit esse cillum dolore eu fugiat nulla pariatur. Excepteur sint occaecat cupidatat non proident, sunt in culpa qui officia deserunt mollit anim id est laborum. updatat non proident, sunt in culpa qui officia deserunt mollit anim id est laborum.</p></div>
      <div class="img-box" role="img" aria-label="Image placeholder"></div>
    </div>
  </div>
  <footer class="foot">Copyright text here</footer>
</section>

</body>
</html>
```